Volren Goods Ltd Stationery Design Project

hi we need to design business cards, letter head, complimentary slips, scribble pads, note pads, envelopes for volren goods ltd.

please see business cards details

Kelvin Obutu

P.O Box 41873 -00312 Nairobi - Kenya
Tel: +254-733-218-904
Email: volrengoods@mailvexo.com

company name should appear on all stationery : Volren Goods Ltd

Industry/Entity Type

Business

Requirements
Must have
• kindly stick to colours in the logo

```html
<!DOCTYPE html>
<html lang="en">
<head>
<meta charset="UTF-8">
<title>Volren Goods Ltd – Business Card</title>
<link rel="stylesheet" href="https://fonts.googleapis.com/css2?family=Poppins:wght@400;600;700&display=swap">
<style>
  :root {
    --brand-blue: #25288f;
    --brand-orange: #f08a12;
    --paper: #f6f6f4;
    --ink: #3a3a3a;
    --divider: #cfcfcf;
    --backdrop: #1c1f3a;
  }
  * { margin: 0; padding: 0; box-sizing: border-box; }
  html, body {
    width: 1200px;
    height: 800px;
    overflow: hidden;
    background: var(--backdrop);
    font-family: "Poppins", sans-serif;
  }
  .canvas {
    width: 1200px;
    height: 800px;
    display: flex;
    align-items: center;
    justify-content: center;
  }
  .business-card {
    position: relative;
    width: 1000px;
    height: 572px;
    background: var(--paper);
    box-shadow: 0 20px 50px rgba(0,0,0,.45);
    overflow: hidden;
  }
  .brand-block {
    position: absolute;
    left: 70px;
    top: 150px;
    width: 400px;
    height: 200px;
    display: flex;
    align-items: center;
    gap: 22px;
  }
  .brand-mark {
    flex: none;
    width: 64px;
    height: 64px;
    border-radius: 50%;
    background: var(--brand-orange);
  }
  .brand-name {
    font-weight: 700;
    font-size: 52px;
    line-height: 1.05;
    color: var(--brand-blue);
    text-transform: uppercase;
    letter-spacing: 2px;
  }
  .card-divider {
    position: absolute;
    left: 520px;
    top: 110px;
    width: 1px;
    height: 240px;
    background: var(--divider);
  }
  .contact-block {
    position: absolute;
    left: 565px;
    top: 112px;
    color: var(--ink);
    font-size: 21px;
    line-height: 1.4;
  }
  .contact-name {
    font-weight: 700;
    font-size: 27px;
    color: var(--brand-blue);
    letter-spacing: .5px;
    text-transform: uppercase;
    margin-bottom: 28px;
  }
  .contact-line .label {
    color: var(--brand-orange);
    font-weight: 700;
    margin-right: 6px;
  }
  .company-address {
    margin-top: 30px;
  }
  .company-address .company {
    text-transform: uppercase;
  }
  .accent-stripe {
    position: absolute;
    left: 0;
    right: 0;
    bottom: 84px;
    height: 12px;
    background: var(--brand-orange);
  }
  .base-band {
    position: absolute;
    left: 0;
    right: 0;
    bottom: 0;
    height: 84px;
    background: var(--brand-blue);
  }
</style>
</head>
<body>
<main class="canvas">
  <section class="business-card">
    <div class="brand-block">
      <span class="brand-mark"></span>
      <div class="brand-name">Volren<br>Goods</div>
    </div>

    <div class="card-divider"></div>

    <div class="contact-block">
      <p class="contact-name">Kelvin Obutu</p>
      <p class="contact-line"><span class="label">T</span>+254-733-218-904</p>
      <p class="contact-line"><span class="label">E</span>volrengoods@mailvexo.com</p>
      <div class="company-address">
        <p class="company">Volren Goods Ltd</p>
        <p>P.O Box 41873 - 00312</p>
        <p>Nairobi - Kenya</p>
      </div>
    </div>

    <div class="accent-stripe"></div>
    <div class="base-band"></div>
  </section>
</main>
</body>
</html>
```